Company or website name
- DOVANTRA
- Links to the website
- WWW.DOVANTRA.NET
- Describe your company and organization and target audience
- check the website: www.dovantra.net
- The design should have the following
- A clean visual is expected. The documents should include the complete address, emails, phone, name and position.
- Other Facts

```html
<!DOCTYPE html>
<html lang="en">
<head>
<meta charset="utf-8">
<title>DOVANTRA – Business Card</title>
<link href="https://fonts.googleapis.com/css2?family=Open+Sans:wght@400;600&display=swap" rel="stylesheet">
<style>
  :root {
    --backdrop: #d8d3ce;
    --frost-light: #f3f4f5;
    --frost-mid: #e3e6e9;
    --navy: #0b3459;
    --navy-deep: #072844;
    --teal: #3f9e8c;
    --sand: #e6d8bf;
    --ivory: #eef0f1;
  }
  * { margin: 0; padding: 0; box-sizing: border-box; }
  html, body {
    width: 1200px; height: 969px; overflow: hidden;
    background: var(--backdrop);
    font-family: "Open Sans", Arial, sans-serif;
  }
  .card {
    position: absolute; left: 100px; top: 198px;
    width: 1000px; height: 572px;
    display: flex;
    box-shadow: 0 18px 40px rgba(0,0,0,0.18);
  }
  .card-front {
    width: 520px; height: 100%;
    background: linear-gradient(160deg, var(--frost-light), var(--frost-mid));
    border: 1px solid rgba(0,0,0,0.12);
    border-right: none;
    display: flex; align-items: center;
    padding-left: 72px;
    overflow: hidden;
  }
  .brand-name {
    font-size: 78px; font-weight: 400;
    color: var(--navy); letter-spacing: 0; line-height: 1;
    white-space: nowrap;
    margin-top: 12px;
  }
  .divider { width: 11px; height: 100%; background: var(--teal); flex: none; }
  .card-details {
    flex: 1; height: 100%;
    background: linear-gradient(170deg, var(--navy), var(--navy-deep));
    padding: 108px 0 0 58px;
  }
  .person-name { font-size: 40px; font-weight: 600; color: var(--sand); line-height: 1.1; }
  .person-role { font-size: 24px; color: var(--teal); line-height: 1.2; }
  .address { margin-top: 42px; font-size: 24px; color: var(--ivory); line-height: 1.3; }
  .contact-list { margin-top: 40px; list-style: none; }
  .contact-list li {
    display: flex; align-items: center; gap: 12px;
    font-size: 24px; color: var(--sand); line-height: 33px;
  }
  .contact-list svg { width: 24px; height: 24px; fill: var(--teal); flex: none; }
</style>
</head>
<body>
  <div class="card">
    <div class="card-front">
      <div class="brand-name">DOVANTRA</div>
    </div>
    <div class="divider"></div>
    <div class="card-details">
      <div class="person-name">Marco Velardi</div>
      <div class="person-role">President</div>
      <div class="address">Los Pinos, Altos del Mar<br>Ciudad Norte</div>
      <ul class="contact-list">
        <li>
          <svg viewBox="0 0 24 24" aria-hidden="true"><path d="M6.6 10.8c1.4 2.8 3.8 5.1 6.6 6.6l2.2-2.2c.3-.3.7-.4 1-.2 1.1.4 2.3.6 3.6.6.6 0 1 .4 1 1V20c0 .6-.4 1-1 1C10.6 21 3 13.4 3 4c0-.6.4-1 1-1h3.5c.6 0 1 .4 1 1 0 1.3.2 2.5.6 3.6.1.3 0 .7-.2 1z"/></svg>
          +507 814-2270
        </li>
        <li>
          <svg viewBox="0 0 24 24" aria-hidden="true"><path d="M7 1h10c1.1 0 2 .9 2 2v18c0 1.1-.9 2-2 2H7c-1.1 0-2-.9-2-2V3c0-1.1.9-2 2-2zm0 3v14h10V4H7zm5 15.5a1.2 1.2 0 100 2.4 1.2 1.2 0 000-2.4z"/></svg>
          +507 6430-5718
        </li>
        <li>
          <svg viewBox="0 0 24 24" aria-hidden="true"><path d="M2 5h20v14H2V5zm2 2v.5l8 5 8-5V7l-8 5-8-5z"/></svg>
          sales@dovantra.net
        </li>
        <li>
          <svg viewBox="0 0 24 24" aria-hidden="true"><path d="M12 2a10 10 0 100 20 10 10 0 000-20zm6.9 6h-3a15 15 0 00-1.4-3.7A8 8 0 0118.9 8zM12 4c.8 1.2 1.5 2.5 1.9 4h-3.8c.4-1.5 1.1-2.8 1.900-4zM4.3 14a8 8 0 010-4h3.4a16 16 0 000 4H4.3zm.8 2h3a15 15 0 001.4 3.7A8 8 0 015.1 16zM8 8H5.1a8 8 0 014.4-3.7C8.9 5.5 8.4 6.7 8 8zm4 12c-.8-1.2-1.5-2.5-1.9-4h3.8c-.4 1.5-1.1 2.8-1.9 4zm2.3-6H9.7a14 14 0 010-4h4.6a14 14 0 010 4zm.2 5.7c.6-1.2 1.1-2.4 1.4-3.7h3a8 8 0 01-4.4 3.7zM16.3 14a16 16 0 000-4h3.4a8 8 0 010 4h-3.4z"/></svg>
          www.dovantra.net
        </li>
      </ul>
    </div>
  </div>
</body>
</html>
```